The Hidden Roots of Lingering Illness Revealed

Subtitle: At last, uncover the reasons behind poor sleep, brain fog, and bloating.

I need an awesome book cover that fits this title.

```html
<!DOCTYPE html>
<html lang="en">
<head>
<meta charset="utf-8">
<title>The Hidden Roots of Lingering Illness Revealed</title>
<link href="https://fonts.googleapis.com/css2?family=Oswald:wght@300;700&family=Poppins:wght@600&display=swap" rel="stylesheet">
<style>
  :root {
    --green-deep: #00503c;
    --green-mid: #05855f;
    --green-glow: #0a8f6a;
    --yellow: #f5cf02;
    --white: #ffffff;
    --ink: #1f1f1f;
    --art-blue-light: #2f86f0;
    --art-blue-dark: #1d55b8;
  }
  * { margin: 0; padding: 0; box-sizing: border-box; }
  html, body {
    width: 927px;
    height: 1200px;
    overflow: hidden;
    background: var(--green-deep);
  }
  .cover {
    position: relative;
    width: 927px;
    height: 1200px;
    overflow: hidden;
    background: radial-gradient(ellipse 70% 55% at 50% 62%, var(--green-glow) 0%, var(--green-mid) 45%, var(--green-deep) 100%);
  }
  .cover-title {
    position: absolute;
    top: 0;
    left: 0;
    width: 927px;
    height: 560px;
  }
  .title-kicker {
    font-family: 'Oswald', sans-serif;
    font-weight: 300;
    fill: var(--white);
  }
  .title-rule { stroke: var(--yellow); stroke-width: 3; }
  .title-main {
    font-family: 'Oswald', sans-serif;
    font-weight: 700;
  }
  .title-white { fill: var(--white); }
  .title-yellow { fill: var(--yellow); }
  .cover-art {
    position: absolute;
    left: 288px;
    top: 595px;
    width: 442px;
    height: 441px;
    background: linear-gradient(180deg, var(--art-blue-light) 0%, var(--art-blue-dark) 100%);
  }
  .cover-band {
    position: absolute;
    left: 0;
    top: 1036px;
    width: 927px;
    height: 164px;
    background: var(--yellow);
    display: flex;
    align-items: center;
    justify-content: center;
  }
  .cover-subtitle {
    font-family: 'Poppins', sans-serif;
    font-weight: 600;
    font-size: 33px;
    line-height: 48px;
    color: var(--ink);
    text-align: center;
    max-width: 790px;
  }
</style>
</head>
<body>
  <main class="cover">
    <svg class="cover-title" viewBox="0 0 927 560" aria-label="The Hidden Roots of Lingering Illness Revealed">
      <line class="title-rule" x1="85" y1="86" x2="250" y2="86"/>
      <line class="title-rule" x1="677" y1="86" x2="841" y2="86"/>
      <text class="title-kicker" x="463.5" y="105" text-anchor="middle" font-size="54" textLength="395" lengthAdjust="spacingAndGlyphs">THE HIDDEN ROOTS OF</text>
      <text class="title-main title-white" x="463.5" y="241" text-anchor="middle" font-size="150" textLength="745" lengthAdjust="spacingAndGlyphs">LINGERING</text>
      <text class="title-main title-yellow" x="463.5" y="460" text-anchor="middle" font-size="255" textLength="734" lengthAdjust="spacingAndGlyphs">ILLNESS</text>
      <text class="title-main title-white" x="463.5" y="545" text-anchor="middle" font-size="82" textLength="520" lengthAdjust="spacing">REVEALED</text>
    </svg>

    <div class="cover-art" role="img" aria-label="Cover artwork: glowing blue human figure seen from behind, with an inflamed neck and shoulder"></div>

    <section class="cover-band">
      <p class="cover-subtitle">At last, uncover the reasons behind poor sleep, brain fog, and bloating.</p>
    </section>
  </main>
</body>
</html>
```